Legal Agribusiness Capability Brochure Design

Design A4 sized 6 page Legal Agribusiness Capability Brochure. Design is to be consistent with current marketing materials - logo, letterhead, website and business card to be provided.
Cover page - Firm name and logo, Agribusiness Capability Statement heading with image 1 below
Inside cover page - About Us section with image 2 below then Awards section below image
Inside middle page - Our Expertise with image 3 below
Inside back page - Our Experience with image 4 below
Back page - Senior Lawyers with image 5 below
Outside Middle Back Page - Contact Us with image 6
Updates

To provide more details to designers for brochure

Target Market(s)

Agribusiness - Australia

Industry/Entity Type

Legal

Colors

Designer to choose colors to be used in the design.

Requirements
Must have
• Use content from uloaded file - Agribusiness Brochure Content
• Use images uploaded
• Professional appearance
• Consistent with current marketing and website https://ferngatelegal.com.au/

```html
<!DOCTYPE html>
<html lang="en">
<head>
<meta charset="utf-8">
<title>Ferngate Legal – Agribusiness Capability Statement</title>
<link href="https://fonts.googleapis.com/css2?family=Montserrat:wght@300;400;600&display=swap" rel="stylesheet">
<style>
  :root{
    --blue:#2e93d1;
    --page:#ededed;
    --page-shade:#e4e4e4;
    --panel:#f7f7f7;
    --grey:#c9c9c9;
    --grey-mid:#bdbdbd;
    --rule:#8a8a8a;
    --ink:#5a5a5a;
    --ink-dark:#3c3c3c;
    --white:#ffffff;
    --backdrop:#e6e6e6;
    --wheat-sky:#a7998f;
    --wheat-haze:#c8b59a;
    --wheat-gold:#d9b35a;
    --wheat-deep:#b98a3a;
    --badge:#e3dcc4;
  }
  *{box-sizing:border-box;margin:0;padding:0}
  html,body{width:1200px;height:862px;overflow:hidden}
  body{background:var(--backdrop);font-family:"Montserrat",sans-serif;color:var(--ink);position:relative}

  .sheet{position:absolute;top:236px;height:390px;display:flex}
  .cover-sheet{left:33px}
  .spread-sheet{left:339px;box-shadow:0 6px 18px rgba(0,0,0,.12)}
  .page{position:relative;width:276px;height:390px;background:var(--page);overflow:hidden}
  .cover{box-shadow:0 6px 18px rgba(0,0,0,.12)}

  .heading{font-weight:600;font-size:11px;line-height:1.2;margin-bottom:8px}
  .cols{display:flex;gap:12px}
  .cols p{flex:1;font-size:5.8px;line-height:1.6}

  /* cover */
  .cover-arc{position:absolute;left:40px;top:95px;width:330px;height:330px;border-radius:50%;background:var(--panel)}
  .brand{position:absolute;left:18px;top:26px;display:flex;align-items:center;gap:8px}
  .brand-mark{width:26px;height:26px;background:var(--blue)}
  .brand-name{font-weight:600;font-size:15px;letter-spacing:.5px;color:var(--blue);line-height:1}
  .brand-tag{position:absolute;left:52px;top:46px;font-size:7px;line-height:1;color:var(--ink)}
  .cover-photo{position:absolute;left:58px;top:112px}
  .award-badge{position:absolute;left:92px;top:300px;width:50px;height:50px;border-radius:50%;background:var(--badge)}
  .cover-title{position:absolute;left:150px;top:298px;font-weight:300;font-size:15px;line-height:1.15;color:var(--ink-dark)}
  .cover-band{position:absolute;left:0;bottom:0;width:276px;height:40px}

  /* about */
  .about-band{position:absolute;left:0;top:0;width:276px;height:118px;background:var(--blue);padding:20px 16px;color:var(--white)}
  .about-photo{position:absolute;left:16px;top:130px;width:244px;height:90px;background:var(--grey)}
  .award-photo{position:absolute;left:16px;top:232px;width:64px;height:60px;background:var(--grey)}
  .awards-table{position:absolute;left:90px;top:232px;width:170px;height:120px;border:1px solid var(--grey-mid);background:var(--white)}
  .awards-table .row{height:10px;border-bottom:1px solid var(--grey-mid)}
  .awards-table .row.head{background:var(--grey)}
  .about-corner{position:absolute;right:0;bottom:0}

  /* expertise */
  .expertise{background:var(--page-shade)}
  .expertise .heading{position:absolute;left:0;top:26px;width:100%;text-align:center;color:var(--ink-dark)}
  .ruled{position:absolute;top:52px;width:112px}
  .ruled.left{left:20px}
  .ruled.right{left:144px}
  .ruled span{display:block;height:12px;border-bottom:1px solid var(--rule)}
  .dots{position:absolute;left:24px;top:300px;display:flex;gap:14px;align-items:flex-end}
  .dot{width:66px;height:66px;border-radius:50%;background:var(--white)}
  .dot:nth-child(1){opacity:.7}
  .dot:nth-child(2){opacity:.85;margin-bottom:14px}
  .dot:nth-child(3){margin-bottom:28px}

  /* experience */
  .experience-text{position:absolute;left:18px;top:24px;width:242px}
  .experience-text .heading{color:var(--ink-dark)}
  .experience-photo{position:absolute;left:64px;top:196px}
</style>
</head>
<body>
  <section class="sheet cover-sheet">
    <article class="page cover">
      <div class="cover-arc"></div>
      <div class="brand"><span class="brand-mark"></span><span class="brand-name">FERNGATE LEGAL</span></div>
      <div class="brand-tag">Commercial + Litigation</div>
      <svg class="cover-photo" width="210" height="170" viewBox="0 0 210 170" role="img" aria-label="Photograph of a yellow combine harvester cutting a golden wheat field under a cloudy sky">
        <defs>
          <linearGradient id="cover-field" x1="0" y1="0" x2="0" y2="1">
            <stop offset="0" stop-color="var(--wheat-sky)"/><stop offset=".45" stop-color="var(--wheat-haze)"/><stop offset=".6" stop-color="var(--wheat-gold)"/><stop offset="1" stop-color="var(--wheat-deep)"/>
          </linearGradient>
        </defs>
        <path d="M30 0H180A30 30 0 0 1 210 30V140A30 30 0 0 1 180 170H125L105 150L85 170H30A30 30 0 0 1 0 140V30A30 30 0 0 1 30 0Z" fill="url(#cover-field)"/>
      </svg>
      <div class="award-badge"></div>
      <h1 class="cover-title">Agribusiness<br>Capability<br>Statement</h1>
      <svg class="cover-band" viewBox="0 0 276 40"><polygon points="120,40 276,5 276,40" fill="var(--blue)"/></svg>
    </article>
  </section>

  <section class="sheet spread-sheet">
    <article class="page about">
      <div class="about-band">
        <h2 class="heading">About Us</h2>
        <div class="cols">
          <p>Ferngate Legal is a regional commercial and litigation firm supporting farming families, producers and rural businesses. Our team understands the land, the seasons and the pressures that shape every decision on the farm. We work alongside clients for the long term, across generations.</p>
          <p>We give clear, practical advice on property, succession, water rights and disputes, so clients can plan with confidence and focus on running a productive operation. Fees are transparent and our lawyers travel to meet clients on site.</p>
        </div>
      </div>
      <div class="about-photo" role="img" aria-label="Image area for the About Us photograph"></div>
      <div class="award-photo" role="img" aria-label="Image area for an awards photograph"></div>
      <div class="awards-table">
        <div class="row head"></div><div class="row"></div><div class="row"></div><div class="row"></div><div class="row"></div><div class="row"></div><div class="row"></div><div class="row"></div><div class="row"></div><div class="row"></div><div class="row"></div>
      </div>
      <svg class="about-corner" width="40" height="40" viewBox="0 0 40 40"><polygon points="40,0 40,40 10,40" fill="var(--blue)"/></svg>
    </article>

    <article class="page expertise">
      <h2 class="heading">Our Agribusiness Expertise</h2>
      <div class="ruled left"><span></span><span></span><span></span><span></span><span></span><span></span><span></span><span></span><span></span><span></span><span></span><span></span><span></span><span></span><span></span><span></span><span></span><span></span></div>
      <div class="ruled right"><span></span><span></span><span></span><span></span><span></span><span></span><span></span><span></span><span></span><span></span><span></span><span></span><span></span><span></span><span></span><span></span><span></span><span></span></div>
      <div class="dots"><span class="dot"></span><span class="dot"></span><span class="dot"></span></div>
    </article>

    <article class="page experience">
      <div class="experience-text">
        <h2 class="heading">Our Agribusiness Experience</h2>
        <div class="cols">
          <p>Our lawyers have acted on farm sales, leases and share farming agreements across the region. We have guided family succession plans, restructured rural holdings and resolved boundary and stock disputes for landholders of every size. We regularly assist with water licences, native vegetation approvals, machinery finance and employment matters for seasonal workers, always with an eye on cash flow and the next harvest.</p>
          <p>We also advise agribusiness lenders, cooperatives and suppliers on contracts, finance and compliance, drawing on years of hands-on work with producers throughout regional Australia. Recent matters include the sale of a mixed cropping enterprise, the restructure of a family grazing company and the defence of a grain contract claim.</p>
        </div>
      </div>
      <svg class="experience-photo" width="196" height="172" viewBox="0 0 196 172" role="img" aria-label="Photograph of a yellow combine harvester in a ripe wheat field">
        <defs>
          <linearGradient id="experience-field" x1="0" y1="0" x2="0" y2="1">
            <stop offset="0" stop-color="var(--wheat-sky)"/><stop offset=".45" stop-color="var(--wheat-haze)"/><stop offset=".6" stop-color="var(--wheat-gold)"/><stop offset="1" stop-color="var(--wheat-deep)"/>
          </linearGradient>
        </defs>
        <path d="M28 0H168A28 28 0 0 1 196 28V144A28 28 0 0 1 168 172H116L98 154L80 172H28A28 28 0 0 1 0 144V28A28 28 0 0 1 28 0Z" fill="url(#experience-field)"/>
      </svg>
    </article>
  </section>
</body>
</html>
```